Need a stunning looking Business Card Design for my Telecom Business, Wow FACTOR!

I deal with high level IT Directors , and Contractors.
I need to impress them with a sleek , professional and unique business card.
Im thinking options as far as rounded edges, plastic , or even metal card or die cut on a corner.
Whatever looks better and leave an unforgettable first impression.
im looking for the wow factor.
Front should have the basics info (attached on the picture of current business card)
i would like to add picture of myself somewhere
Back side
should have logo and maybe some pictures or past projects, you can download from my website ( www.lumvexholdings.com)

```html
<!DOCTYPE html>
<html lang="en">
<head>
<meta charset="utf-8">
<title>Lumvex Technologies – Business Card</title>
<link rel="stylesheet" href="https://fonts.googleapis.com/css2?family=Lato:wght@400;700&family=Montserrat:wght@400;500;600&display=swap">
<style>
  :root {
    --navy: #1b2a56;
    --navy-panel: #1c2a57;
    --blue-band-top: #1f4f8e;
    --blue-band-bottom: #1a4580;
    --orange: #f7931e;
    --orange-dark: #e57e0c;
    --paper: #ffffff;
    --panel-grey: #ebebeb;
    --back-grey: #f2f2f2;
    --line-grey: #d2d2d2;
    --ink: #1d1d1f;
    --canvas: #ececec;
  }
  * { margin: 0; padding: 0; box-sizing: border-box; }
  html, body { width: 1200px; height: 1200px; overflow: hidden; }
  body { background: var(--canvas); position: relative; font-family: "Montserrat", Arial, sans-serif; }

  .card {
    position: absolute;
    left: 201px;
    width: 721px;
    height: 432px;
    border-radius: 20px;
    overflow: hidden;
    transform: scale(1.1111);
    transform-origin: top left;
  }
  .card--front { top: 64px; background: var(--paper); }
  .card--back { top: 629px; background: var(--back-grey); }
  .card__art { position: absolute; inset: 0; width: 100%; height: 100%; }

  /* Front */
  .brand-name {
    position: absolute;
    left: 62px; top: 104px;
    display: flex; align-items: center; gap: 8px;
    font-family: "Montserrat", Arial, sans-serif;
    font-weight: 500;
    font-size: 15px;
    letter-spacing: 1.5px;
    color: var(--ink);
  }
  .brand-name__mark { width: 12px; height: 12px; background: var(--orange); }

  .contact { position: absolute; left: 59px; top: 190px; list-style: none; color: #fff; }
  .contact__item { position: absolute; left: 0; display: flex; align-items: flex-start; gap: 16px; white-space: nowrap; }
  .contact__item--place { top: 0; }
  .contact__item--phone { top: 51px; }
  .contact__item--mail { top: 122px; }
  .contact__item--web { top: 158px; }
  .contact__icon {
    width: 28px; height: 28px; flex: none;
    background: linear-gradient(180deg, var(--orange), var(--orange-dark));
    border: 1px solid #ffb35a;
    display: flex; align-items: center; justify-content: center;
  }
  .contact__text { font-size: 15.5px; line-height: 20.5px; font-weight: 400; }
  .contact__item--mail .contact__text,
  .contact__item--web .contact__text { font-size: 16.5px; line-height: 28px; }

  .person { position: absolute; right: 89px; top: 253px; text-align: right; font-family: "Lato", Arial, sans-serif; }
  .person__name { font-size: 25px; color: #fff; letter-spacing: 0.3px; line-height: 28px; }
  .person__name strong { font-weight: 700; }
  .person__name span { font-weight: 400; }
  .person__role { font-size: 18.5px; color: var(--orange); letter-spacing: 0.3px; line-height: 22px; }

  /* Back */
  .back-brand {
    position: absolute; left: 0; right: 0; top: 200px;
    display: flex; align-items: center; justify-content: center; gap: 12px;
    font-family: "Montserrat", Arial, sans-serif;
    font-weight: 500; font-size: 27px; letter-spacing: 2px;
    color: var(--ink);
  }
  .back-brand__mark { width: 18px; height: 18px; background: var(--orange); }
  .tagline {
    position: absolute; left: 0; right: 0; top: 329px;
    text-align: center;
    font-family: "Lato", Arial, sans-serif;
    font-size: 19px; letter-spacing: 0.4px; color: #fff;
  }
</style>
</head>
<body>

<section class="card card--front" aria-label="Business card front">
  <svg class="card__art" viewBox="0 0 721 432" aria-hidden="true">
    <defs>
      <linearGradient id="band-gradient" x1="0" y1="0" x2="1" y2="0">
        <stop offset="0" stop-color="#1c2c5c"/>
        <stop offset="0.45" stop-color="#1e4578"/>
        <stop offset="1" stop-color="#2a82b3"/>
      </linearGradient>
    </defs>
    <polygon points="497,0 721,0 721,169 422,169" fill="var(--panel-grey)"/>
    <line x1="487" y1="0" x2="412" y2="169" stroke="var(--line-grey)" stroke-width="3"/>
    <polygon points="0,169 424,169 367,277 424,384 0,384" fill="url(#band-gradient)"/>
    <polygon points="424,169 440,169 383,277 440,384 424,384 367,277" fill="var(--orange)"/>
    <polygon points="440,169 721,169 721,384 440,384 383,277" fill="var(--navy-panel)"/>
    <polygon points="442,384 721,384 721,432 462,432" fill="var(--panel-grey)"/>
    <line x1="432" y1="384" x2="452" y2="432" stroke="var(--line-grey)" stroke-width="3"/>
    <polygon points="673,255 656,276 673,297" fill="var(--orange)"/>
  </svg>

  <div class="brand-name"><span class="brand-name__mark"></span>LUMVEX TECHNOLOGIES</div>

  <ul class="contact">
    <li class="contact__item contact__item--place">
      <span class="contact__icon">
        <svg width="14" height="18" viewBox="0 0 14 18"><path d="M7 1a5.5 5.5 0 0 0-5.5 5.5C1.5 11 7 17 7 17s5.5-6 5.5-10.5A5.5 5.5 0 0 0 7 1z" fill="#fff"/><circle cx="7" cy="6.5" r="2.2" fill="var(--orange)"/></svg>
      </span>
      <span class="contact__text">Offices in Miami, Broward<br>and Palm Beach</span>
    </li>
    <li class="contact__item contact__item--phone">
      <span class="contact__icon">
        <svg width="18" height="16" viewBox="0 0 18 16"><path d="M2 5c0-2 3-3 7-3s7 1 7 3v1.5h-3.5V5h-7v1.5H2z" fill="#fff"/><path d="M4 8h10l1.5 6h-13z" fill="#fff"/><circle cx="9" cy="11" r="1.8" fill="var(--orange)"/></svg>
      </span>
      <span class="contact__text">(305) 555-0147 Miami<br>(954) 555-0183 Broward<br>(561) 555-0129 Palm Beach</span>
    </li>
    <li class="contact__item contact__item--mail">
      <span class="contact__icon">
        <svg width="18" height="13" viewBox="0 0 18 13"><rect x="1" y="1" width="16" height="11" fill="none" stroke="#fff" stroke-width="1.6"/><path d="M1 1l8 6 8-6" fill="none" stroke="#fff" stroke-width="1.6"/></svg>
      </span>
      <span class="contact__text">Info@lumvexholdings.com</span>
    </li>
    <li class="contact__item contact__item--web">
      <span class="contact__icon">
        <svg width="18" height="18" viewBox="0 0 18 18" fill="none" stroke="#fff" stroke-width="1.4"><circle cx="9" cy="9" r="7.5"/><ellipse cx="9" cy="9" rx="3.5" ry="7.5"/><line x1="1.5" y1="9" x2="16.5" y2="9"/><line x1="9" y1="1.5" x2="9" y2="16.5"/></svg>
      </span>
      <span class="contact__text">www.lumvexholdings.com</span>
    </li>
  </ul>

  <div class="person">
    <p class="person__name"><strong>DARIO</strong> <span>KESSLER</span></p>
    <p class="person__role">OPERATIONS MANAGER</p>
  </div>
</section>

<section class="card card--back" aria-label="Business card back">
  <svg class="card__art" viewBox="0 0 721 432" aria-hidden="true">
    <defs>
      <linearGradient id="back-band-gradient" x1="0" y1="0" x2="0" y2="1">
        <stop offset="0" stop-color="var(--blue-band-top)"/>
        <stop offset="1" stop-color="var(--blue-band-bottom)"/>
      </linearGradient>
    </defs>
    <rect x="0" y="314" width="721" height="118" fill="url(#back-band-gradient)"/>
    <rect x="0" y="314" width="721" height="13" fill="var(--navy)"/>
    <polygon points="159,314 562,314 536,372 185,372" fill="var(--navy)"/>
  </svg>

  <div class="back-brand"><span class="back-brand__mark"></span>LUMVEX TECHNOLOGIES</div>
  <p class="tagline">LOW VOLTAGE CONTRACTOR</p>
</section>

</body>
</html>
```